a residential cleaning service needs a website

We need a website for our faith based residential cleaning service, we are called MARGOT'S CLEANING SERVICE. We want a website that is clean looking both for mobile version and desktop. We want to convey cleanliness and trust to our clients. The color scheme should go in hand with the colors of the LOGO. We would like an about page, statement of faith page, services page and also a page for a booking module that our CRM has provided for us to being able to code and dress said module is important. The website not only needs to market to new customers and convey our service but also be easy to use for existing clients to schedule cleanings and services.
Industry/Entity Type
Cleaning Service
Coding
Coded - Design and coding required
Number of Pages Required
4 page
Requirements
Must have
- About page
Statement of Faith page
services page
booking and login page

```html
<!DOCTYPE html>
<html lang="en">
<head>
<meta charset="utf-8">
<title>Margot's Cleaning Service</title>
<link rel="stylesheet" href="https://fonts.googleapis.com/css2?family=Poppins:wght@300;400;500;600&display=swap">
<style>
:root{
  --navy:#0e3f8e;
  --blue:#0a5ad4;
  --blue-bright:#1f6ff0;
  --ink:#2a2d3e;
  --muted:#5b5f70;
  --pale:#eef2fa;
  --footer:#1a2247;
  --white:#ffffff;
}
*{box-sizing:border-box;margin:0;padding:0}
html,body{width:1200px;height:3943px;overflow:hidden}
body{font-family:"Poppins",sans-serif;color:var(--ink);background:var(--white)}
.page{position:relative;width:1200px;height:3943px;overflow:hidden}
.abs{position:absolute}
.photo{position:absolute}
/* hero */
.hero-photo{left:0;top:0;width:600px;height:664px;background:linear-gradient(160deg,#f4f1ec 0%,#e8e3dc 45%,#f2b623 70%,#2f7fd8 100%)}
.hero-panel{left:600px;top:0;width:600px;height:664px;background:var(--navy);overflow:hidden}
.hero-waves{position:absolute;left:0;top:440px;width:600px;height:224px;background:linear-gradient(180deg,rgba(14,63,142,0) 0%,#1a5bb3 45%,#2a7fd4 100%)}
.brand{position:absolute;left:50px;top:42px;display:flex;align-items:center;gap:10px;color:var(--navy);font-weight:600;font-size:15px;line-height:1.2;width:190px}
.brand .dot{width:40px;height:40px;border-radius:50%;background:var(--navy);flex:none}
.nav{position:absolute;top:38px;color:var(--white);font-size:15px}
.btn-booking{position:absolute;left:1030px;top:30px;width:116px;height:42px;border-radius:21px;background:var(--white);color:var(--ink);font-size:15px;display:flex;align-items:center;justify-content:center}
.hero-sub{position:absolute;left:600px;width:600px;top:255px;text-align:center;color:var(--white);font-size:30px;font-weight:300}
.hero-title{position:absolute;left:600px;width:600px;top:300px;text-align:center;color:var(--white);font-size:62px;font-weight:500}
.btn-hero{position:absolute;left:814px;top:411px;width:182px;height:40px;border-radius:20px;background:var(--blue-bright);color:var(--white);font-size:16px;display:flex;align-items:center;justify-content:center}
/* who */
.who-dots{left:128px;top:748px;width:90px;height:95px;background:#eceff4}
.who-arc{left:430px;top:760px}
.who-img1{left:147px;top:766px;width:290px;height:318px;background:linear-gradient(180deg,#dfe3e6,#b8c3cc 60%,#3b8fd6)}
.who-img2{left:340px;top:865px;width:248px;height:280px;background:linear-gradient(180deg,#e8ebee,#6a8fc4 60%,#244f95);box-shadow:0 10px 30px rgba(0,0,0,.15)}
.play{left:313px;top:968px;width:50px;height:50px;border-radius:50%;background:var(--white);box-shadow:0 4px 12px rgba(0,0,0,.2)}
h2.who{position:absolute;left:667px;top:788px;font-size:28px;font-weight:500}
.who-lead{position:absolute;left:667px;top:838px;width:420px;font-size:19px;font-weight:500;line-height:27px}
.who-h4{position:absolute;left:667px;top:944px;font-size:17px}
.who-p{position:absolute;left:667px;top:978px;width:400px;font-size:14px;line-height:24.5px;color:var(--muted)}
.btn-square{position:absolute;background:var(--blue);color:var(--white);display:flex;align-items:center;justify-content:center;gap:8px;font-size:15px}
.arrow-dot{width:15px;height:15px;border-radius:50%;background:var(--white);display:inline-block;position:relative}
.arrow-dot::after{content:"";position:absolute;left:4px;top:4px;width:4px;height:4px;border-top:2px solid var(--blue);border-right:2px solid var(--blue);transform:rotate(45deg)}
/* services */
.services-bg{left:0;top:1230px;width:1200px;height:720px;background:var(--pale)}
.section-title{position:absolute;left:0;width:1200px;text-align:center;font-size:32px;font-weight:500}
.section-sub{position:absolute;left:0;width:1200px;text-align:center;font-size:16px;color:var(--muted);line-height:26px}
.card{position:absolute;background:var(--white);text-align:center;box-shadow:0 8px 30px rgba(20,40,90,.08);padding:0 30px}
.card h3{font-size:17px;font-weight:500;margin-bottom:16px}
.card p{font-size:12.5px;line-height:21px}
.card.active{background:var(--blue);color:var(--white)}
.card-art{width:110px;height:110px;margin:20px auto 0;border-radius:8px}
.art-vacuum{background:linear-gradient(150deg,#e4f5f3,#8fd6cf)}
.art-spray{width:150px;margin-top:46px;background:linear-gradient(150deg,#2a6fe0,#0d3f99)}
.art-sponge{background:linear-gradient(150deg,#fdf1c4,#9dc2f5)}
.dot-s{position:absolute;border-radius:50%;background:#8b97b0}
/* faith */
.faith-photo{left:0;top:2138px;width:620px;height:421px;background:linear-gradient(180deg,#f2f4f6,#d8dee3 55%,#3aa646)}
.faith-panel{left:0;top:2100px;width:1200px;height:459px}
.faith-title{position:absolute;left:612px;top:2195px;color:var(--white);font-size:31px;font-weight:500}
.faith-lead{position:absolute;left:612px;top:2252px;width:470px;color:var(--white);font-size:17px;line-height:28px}
.faith-p{position:absolute;left:612px;top:2365px;width:470px;color:#dde6f7;font-size:13.5px;line-height:24px}
/* cta */
.cta{left:116px;top:2668px;width:966px;height:162px;background:linear-gradient(90deg,#1466e6,#2a82f2);overflow:hidden}
.cta h2{position:absolute;left:78px;top:44px;color:var(--white);font-size:32px;font-weight:600}
.cta p{position:absolute;left:78px;top:96px;color:#e3edff;font-size:16px}
.btn-white{position:absolute;left:640px;top:50px;width:228px;height:56px;background:var(--white);color:var(--ink);font-size:19px;display:flex;align-items:center;justify-content:center;gap:14px}
.btn-white .arrow-dot{background:var(--blue-bright)}
.btn-white .arrow-dot::after{border-color:var(--white)}
/* contact */
.contact-photo{left:115px;top:2916px;width:436px;height:539px;background:linear-gradient(180deg,#fff,#f3d7b7 35%,#f1a12e 65%,#e9edf1)}
.kicker{position:absolute;left:615px;top:3022px;font-size:13px;color:var(--blue)}
.contact-h{position:absolute;left:615px;top:3048px;font-size:30px;font-weight:600;color:#0b3a8a;line-height:40px}
.contact-h span{font-weight:400;display:block}
.field{position:absolute;border:1px solid #d9dde5;background:var(--white);font-size:12px;color:#6b7080;padding:12px 10px}
/* footer */
.footer{left:0;top:3559px;width:1200px;height:384px;background:var(--footer);color:var(--white)}
.footer h5{position:absolute;font-size:15px;font-weight:600}
.f-txt{position:absolute;font-size:13px;color:#d3d8ea;line-height:22px}
.f-link{position:absolute;font-size:13px;color:#c9cfe4}
.f-brand{position:absolute;left:330px;top:110px;width:130px;text-align:center;font-size:13px;font-weight:600;line-height:17px;color:var(--white)}
.f-brand .dot{width:34px;height:34px;border-radius:50%;border:2px solid var(--white);margin:0 auto 6px}
.sub-input{position:absolute;left:750px;top:164px;width:215px;height:36px;background:#e9edf5;border-radius:18px 0 0 18px;font-size:13px;color:#8a90a4;padding:9px 24px}
.sub-btn{position:absolute;left:962px;top:164px;width:120px;height:36px;background:var(--blue-bright);border-radius:0 18px 18px 0;font-size:14px;font-weight:500;display:flex;align-items:center;justify-content:center}
.social{position:absolute;top:314px;width:10px;height:10px;border-radius:50%;background:#aeb5cc}
</style>
</head>
<body>
<div class="page">

  <!-- hero -->
  <div class="photo hero-photo" role="img" aria-label="Smiling cleaner in a yellow shirt holding a blue broom"></div>
  <div class="brand"><span class="dot"></span><span>MARGOT'S CLEANING SERVICE</span></div>
  <div class="abs hero-panel">
    <div class="hero-waves" role="img" aria-label="Decorative blue waves with floating bubbles"></div>
  </div>
  <div class="nav" style="left:635px">About Us</div>
  <div class="nav" style="left:730px">Faith</div>
  <div class="nav" style="left:796px">Services</div>
  <div class="nav" style="left:940px;display:flex;align-items:center;gap:7px">
    <svg width="11" height="13" viewBox="0 0 11 13"><rect x="0" y="5.5" width="11" height="7.5" rx="1" fill="#fff"/><path d="M2.5 5.5V3.8a3 3 0 0 1 6 0V5.5" fill="none" stroke="#fff" stroke-width="1.6"/></svg>Login</div>
  <div class="btn-booking">Booking</div>
  <div class="hero-sub">An expert cleaning services</div>
  <div class="hero-title">you can trust</div>
  <div class="btn-hero">Take Our Service</div>

  <!-- who we are -->
  <div class="abs who-dots" role="img" aria-label="Decorative dot grid"></div>
  <svg class="abs who-arc" width="170" height="170"><path d="M10 10 A150 150 0 0 1 160 160 L110 160 A100 100 0 0 0 10 60Z" fill="#f1f3f7"/></svg>
  <div class="photo who-img1" role="img" aria-label="Cleaner mopping a kitchen floor"></div>
  <div class="photo who-img2" role="img" aria-label="Team of uniformed cleaning staff with supplies"></div>
  <div class="abs play"><svg width="50" height="50"><path d="M20 16 L34 25 L20 34Z" fill="#2a2d3e"/></svg></div>
  <h2 class="who">Who We Are</h2>
  <div class="who-lead">Margot's Cleaning Service is a faith based cleaning business founded in middle Tennessee over 19 years ago.</div>
  <div class="who-h4">We supply everything</div>
  <div class="who-p">Margot's Cleaning Service provides all equipment and cleaning supplies needed to clean your home to the highest standards</div>
  <div class="btn-square" style="left:667px;top:1080px;width:163px;height:48px">Learn More <span class="arrow-dot"></span></div>

  <!-- services -->
  <div class="abs services-bg"></div>
  <svg class="abs" style="left:0;top:1600px" width="1200" height="350" viewBox="0 0 1200 350" preserveAspectRatio="none">
    <path d="M0 150 C200 60 330 90 520 180 C700 265 900 230 1200 180 L1200 350 L0 350Z" fill="#fff"/>
  </svg>
  <div class="section-title" style="top:1300px">Our Services</div>
  <div class="section-sub" style="top:1348px">Highly Trained, and screened employees</div>

  <div class="card" style="left:118px;top:1466px;width:300px;height:317px">
    <div class="card-art art-vacuum" role="img" aria-label="Vacuum cleaner illustration"></div>
    <h3 style="margin-top:14px">Move in Move out</h3>
    <p>We understand that moving is a daunting process and we are delighted to offer services if that means less stress for you. From ceiling to floor, we will take care of it!</p>
  </div>

  <div class="card active" style="left:450px;top:1431px;width:300px;height:387px">
    <div class="card-art art-spray" role="img" aria-label="Spray bottle and gloved hand illustration"></div>
    <h3 style="margin-top:14px">One time cleaning</h3>
    <p>Planning a party, hosting the in-laws, or just too busy to clean this week? We've got you covered! We offer our detailed cleaning expertise to those who aren't looking for a regular service.</p>
  </div>

  <div class="card" style="left:782px;top:1466px;width:300px;height:317px">
    <div class="card-art art-sponge" role="img" aria-label="Sponge wiping a plate illustration"></div>
    <h3 style="margin-top:14px">Routine Cleaning Service</h3>
    <p>We can design a cleaning plan for you. Once a month, bi- monthly, weekly, whatever you need we are there to help! Each cleaning service will be thorough and leave you satisfied.</p>
  </div>
  <div class="dot-s" style="left:574px;top:1862px;width:8px;height:8px"></div>
  <div class="dot-s" style="left:594px;top:1860px;width:12px;height:12px;background:var(--blue)"></div>
  <div class="dot-s" style="left:618px;top:1862px;width:8px;height:8px"></div>

  <div class="section-title" style="top:1960px">We Supply Everything</div>
  <div class="section-sub" style="top:2008px">Margot's Cleaning Service provides all equipment and cleaning supplies<br>needed to clean your home to the highest standards.</div>

  <!-- faith -->
  <div class="photo faith-photo" role="img" aria-label="Smiling cleaner in a green apron holding a spray bottle"></div>
  <svg class="abs faith-panel" width="1200" height="459" viewBox="0 0 1200 459">
    <defs><linearGradient id="fg" x1="0" x2="1"><stop offset="0" stop-color="#1747a0"/><stop offset="1" stop-color="#2f5fae"/></linearGradient></defs>
    <path d="M600 0 L1200 0 L1200 459 L436 459Z" fill="url(#fg)"/>
  </svg>
  <div class="faith-title">Statement of Faith</div>
  <div class="faith-lead">As a faith based business Margot's Cleaning Service clings to Colossians 3:23 " And whatsoever ye do, do it heartily as to The Lord and not unto men."</div>
  <div class="faith-p">Therefore every job that we do we as a business we pray that the job we perform is pleasing to God. Not only do we see every job as an opportunity to glorify God, but we see every client as a member of the family and look for opportunities to show love and be a light in a dark world.</div>

  <!-- cta -->
  <svg class="abs" style="left:0;top:2600px" width="1200" height="340" viewBox="0 0 1200 340" preserveAspectRatio="none">
    <path d="M0 0 L1200 0 L1200 200 C1000 240 820 300 600 280 C400 262 200 250 0 240Z" fill="#f1f4fa"/>
  </svg>
  <div class="abs cta">
    <h2>Get Started Today!</h2>
    <p>Choose Your Affordable Pricing Plan</p>
    <div class="btn-white">Online Booking <span class="arrow-dot"></span></div>
  </div>

  <!-- contact -->
  <div class="photo contact-photo" role="img" aria-label="Smiling cleaner holding a bucket of supplies and a broom"></div>
  <div class="kicker">Have you Any Question?</div>
  <div class="contact-h">You Can Contact Us<span>If You Have Any Query</span></div>
  <div class="field" style="left:615px;top:3150px;width:228px;height:38px">Name*</div>
  <div class="field" style="left:853px;top:3150px;width:229px;height:38px">Phone*</div>
  <div class="field" style="left:615px;top:3202px;width:228px;height:38px">E-mail*</div>
  <div class="field" style="left:853px;top:3202px;width:229px;height:38px">Select Service
    <svg width="10" height="6" style="position:absolute;right:14px;top:16px"><path d="M1 1 L5 5 L9 1" fill="none" stroke="#333" stroke-width="1.4"/></svg></div>
  <div class="field" style="left:615px;top:3253px;width:467px;height:140px">Write Comment . . .</div>
  <div class="btn-square" style="left:616px;top:3421px;width:163px;height:47px">Submit Now <span class="arrow-dot"></span></div>

  <!-- footer -->
  <div class="abs footer">
    <h5 style="left:118px;top:62px">Contact Us</h5>
    <svg class="abs" style="left:118px;top:102px" width="14" height="18"><path d="M7 17 C2 10 1 8 1 6 a6 6 0 0 1 12 0 c0 2-1 4-6 11Z" fill="none" stroke="#d3d8ea" stroke-width="1.4"/><circle cx="7" cy="6" r="2" fill="#d3d8ea"/></svg>
    <div class="f-txt" style="left:144px;top:98px">245 Harbor Lane #4<br>Austin 78701 TX</div>
    <svg class="abs" style="left:117px;top:160px" width="18" height="18"><path d="M3 1 L7 1 L8 6 L5.5 7.5 C7 10.5 8.5 12 11.5 13.5 L13 11 L18 12 L18 16 C10 17 1 8 2 1Z" fill="#d3d8ea"/></svg>
    <div class="f-txt" style="left:144px;top:157px">(555) 010-0000</div>
    <svg class="abs" style="left:117px;top:210px" width="17" height="12"><rect x=".7" y=".7" width="15.6" height="10.6" fill="none" stroke="#d3d8ea" stroke-width="1.3"/><path d="M1 1 L8.5 7 L16 1" fill="none" stroke="#d3d8ea" stroke-width="1.3"/></svg>
    <div class="f-txt" style="left:144px;top:204px">hello@margotsclean.example</div>

    <div class="f-brand"><div class="dot"></div>MARGOT'S CLEANING SERVICE</div>

    <h5 style="left:556px;top:62px">Quick Links</h5>
    <div class="f-link" style="left:556px;top:98px">Home</div>
    <div class="f-link" style="left:556px;top:126px">About</div>
    <div class="f-link" style="left:556px;top:154px">Services</div>
    <div class="f-link" style="left:556px;top:182px">Contact Us</div>
    <div class="f-link" style="left:556px;top:210px">Call To Us</div>

    <h5 style="left:755px;top:62px">WRITE TO US</h5>
    <div class="f-txt" style="left:755px;top:96px;font-size:11.5px">Provide your email below to<br>subscribe to our newsletter</div>
    <div class="sub-input">Email address</div>
    <div class="sub-btn">Subscribe</div>

    <div class="f-txt" style="left:118px;top:308px">Copyright 2020 &nbsp;Margots cleaning Service</div>
    <div class="social" style="left:955px"></div>
    <div class="social" style="left:980px"></div>
    <div class="social" style="left:1005px"></div>
    <div class="social" style="left:1030px"></div>
    <div class="social" style="left:1055px"></div>
  </div>
</div>
</body>
</html>
```